Creativity training company needs graphic design elements to build visual brand.

The company's name is Mindwave Labs (ML as in special effects for movies or television). I teach and facilitate creative thinking mindset, skills and processes (like design thinking). I am looking for 2-3 graphic design elements to use in print documents, visual presentations and on website that coordinate with new logo. I want the designs to build on the theme of ML - an explosion of creativity or igniting creative ideas. I've been using the words ignite, spark and burst in my copy. I'm open to colour combinations - though I have been considering a lime green or citrus yellow. The blue used in logo is #27aae1.

Target Market(s)

Senior level managers in corporate setting.

Requirements
Must have
• Must coordinate with new logo and theme of ML (special effects)
Nice to have
• Something related to explosion, spark, ignite.
Should not have
• Please note - I am not looking for a new logo or alterations for my current logo (attached) - but rather 2-3 graphic elements or designs that can coordinate WITH my logo and be used independently on website and powerpoint presentations to develop a consistent visual brand.

```html
<!DOCTYPE html>
<html lang="en">
<head>
<meta charset="utf-8">
<title>Mindwave Labs – Burst Graphic Elements</title>
<link href="https://fonts.googleapis.com/css2?family=Source+Sans+3:wght@600&display=swap" rel="stylesheet">
<style>
  :root {
    --page: #ffffff;
    --green-bright: #0cf52c;
    --green-mid: #3ed423;
    --green-deep: #78b61a;
    --burst-core: rgba(160, 245, 80, 0.85);
    --burst-halo: rgba(150, 240, 70, 0.35);
    --logo-grey: #7b7e83;
    --brand-blue: #27aae1;
    --tagline: #ffffff;
  }
  * { margin: 0; padding: 0; box-sizing: border-box; }
  html, body {
    width: 1200px;
    height: 1200px;
    overflow: hidden;
    background: var(--page);
  }
  .canvas {
    position: relative;
    width: 1200px;
    height: 1200px;
    background: var(--page);
    font-family: "Source Sans 3", sans-serif;
  }
  .panel {
    position: absolute;
    overflow: hidden;
    background: linear-gradient(200deg, var(--green-bright) 0%, var(--green-mid) 50%, var(--green-deep) 100%);
  }
  .panel--banner { left: 0; top: 78px; width: 1200px; height: 444px; }
  .panel--tagline { left: 0; top: 560px; width: 584px; height: 584px; }
  .panel--plain { left: 618px; top: 558px; width: 582px; height: 586px; }

  .burst {
    position: absolute;
    inset: 0;
    background:
      radial-gradient(ellipse 22% 22% at 50% 52%, var(--burst-core), transparent 100%),
      radial-gradient(ellipse 45% 45% at 50% 52%, var(--burst-halo), transparent 100%);
  }
  .panel--banner .burst {
    background:
      radial-gradient(ellipse 18% 30% at 50% 55%, var(--burst-core), transparent 100%),
      radial-gradient(ellipse 48% 60% at 50% 55%, var(--burst-halo), transparent 100%);
  }

  .wordmark {
    position: absolute;
    left: 0;
    right: 0;
    top: 176px;
    display: flex;
    align-items: center;
    justify-content: center;
    gap: 22px;
  }
  .wordmark__dot {
    width: 44px;
    height: 44px;
    border-radius: 50%;
    background: var(--brand-blue);
  }
  .wordmark__name {
    font-size: 92px;
    font-weight: 600;
    line-height: 1;
    color: var(--logo-grey);
    letter-spacing: -1px;
  }

  .tagline {
    position: absolute;
    left: 118px;
    top: 288px;
    font-size: 31px;
    font-weight: 600;
    color: var(--tagline);
    letter-spacing: 0.5px;
    white-space: nowrap;
  }
</style>
</head>
<body>
  <main class="canvas">
    <section class="panel panel--banner">
      <div class="burst" role="img" aria-label="Radiating light-green burst of sparks exploding from the centre"></div>
      <div class="wordmark">
        <span class="wordmark__dot"></span>
        <span class="wordmark__name">Mindwave Labs</span>
      </div>
    </section>

    <section class="panel panel--tagline">
      <div class="burst" role="img" aria-label="Radiating light-green burst of sparks exploding from the centre"></div>
      <p class="tagline">ignite, spark and burst</p>
    </section>

    <section class="panel panel--plain">
      <div class="burst" role="img" aria-label="Radiating light-green burst of sparks exploding from the centre"></div>
    </section>
  </main>
</body>
</html>
```